Volt'n Electrical Business Card Design

FRONT OF CARD: should highlight the company logo ( please use image attached) and in small font in the bottom corner must have REC 48193

BACK OF CARD : Company logo at the top, underneath the logo have my name Owen Tate under my name in smaller font Qualified Electrician.
Details to also include are Mobile: 0438257109 E-mail: voltnelectrical@mailbox-example.net

Front and back of card please try to use similar colours as used in the logo. (Blues, greys, black and white)

The logo was created on this website so if you need a different file type of the logo please notify me.

Thanks, Owen

Industry/Entity Type

Business

Contact Information for Business Card

Details are in project description.

Colors
3176b5

Requirements
Must have
• Company logo and contact details

```html
<!DOCTYPE html>
<html lang="en">
<head>
<meta charset="utf-8">
<title>Volt'n Electrical – Business Card</title>
<link rel="stylesheet" href="https://fonts.googleapis.com/css2?family=Open+Sans:wght@400;600;700&display=swap">
<style>
  :root {
    --bg: #e6e3de;
    --card: #f4f5f6;
    --card-edge: #dfe2e6;
    --navy: #1f4670;
    --navy-deep: #173858;
    --brand-blue: #3176b5;
    --sky: #8fd0e0;
    --frame: #ffffff;
    --frame-line: #cfd4da;
    --white: #ffffff;
  }
  * { box-sizing: border-box; margin: 0; padding: 0; }
  html, body {
    width: 1200px; height: 818px; overflow: hidden;
    background: var(--bg);
    font-family: "Open Sans", Arial, sans-serif;
  }
  .stage {
    width: 1200px; height: 818px;
    display: flex; align-items: center; justify-content: center;
  }
  .card {
    position: relative;
    width: 1000px; height: 572px;
    background: linear-gradient(180deg, var(--white) 0%, var(--card) 100%);
    box-shadow: 0 14px 40px rgba(0,0,0,.18);
    overflow: hidden;
  }
  .card__header {
    position: absolute; left: 0; right: 0; top: 0; height: 170px;
  }
  .brand {
    position: absolute; left: 64px; top: 58px;
    display: flex; align-items: center; gap: 16px;
  }
  .brand__mark {
    width: 30px; height: 30px; border-radius: 50%;
    background: var(--brand-blue);
  }
  .brand__name {
    font-size: 50px; font-weight: 700; color: var(--brand-blue);
    letter-spacing: 1px;
  }
  .person {
    position: absolute; right: 60px; top: 46px; text-align: right;
  }
  .person__name {
    font-size: 44px; font-weight: 700; color: var(--navy); line-height: 1.1;
  }
  .person__role {
    font-size: 25px; font-weight: 400; color: var(--sky); margin-top: 2px;
  }
  .divider {
    position: absolute; left: 0; right: 0; top: 180px; height: 6px;
    background: var(--card-edge);
  }
  .gallery {
    position: absolute; left: 36px; right: 36px; top: 200px; height: 232px;
    display: grid; grid-template-columns: repeat(4, 1fr); gap: 18px;
  }
  .gallery__frame {
    background: var(--frame);
    border: 1px solid var(--frame-line);
    padding: 8px;
  }
  .gallery__photo { width: 100%; height: 100%; }
  .photo--cables { background: linear-gradient(135deg, #b9bec6 0%, #6f8fb0 40%, #c98a5a 70%, #d7dadf 100%); }
  .photo--spark  { background: radial-gradient(circle at 50% 50%, #ffd46a 0%, #e0692a 22%, #3a1a10 60%, #0d0d0f 100%); }
  .photo--hand   { background: radial-gradient(circle at 35% 45%, #7fb0ff 0%, #1b3f9e 25%, #0b0f1f 65%, #111 100%); }
  .photo--bulb   { background: radial-gradient(circle at 60% 45%, #dfe9ff 0%, #2a5fd6 25%, #0d2370 60%, #081030 100%); }
  .contact-band {
    position: absolute; left: 0; right: 0; bottom: 0; height: 112px;
    background: linear-gradient(180deg, var(--navy) 0%, var(--navy-deep) 100%);
    display: flex; align-items: center; justify-content: center; gap: 22px;
    color: var(--white); font-size: 27px; font-weight: 400;
  }
  .contact-band__item { display: flex; align-items: center; gap: 12px; }
  .contact-band__sep { width: 1px; height: 30px; background: rgba(255,255,255,.6); }
  .icon { width: 24px; height: 24px; fill: var(--white); }
</style>
</head>
<body>
<main class="stage">
  <article class="card">
    <header class="card__header">
      <div class="brand">
        <span class="brand__mark"></span>
        <span class="brand__name">Volt'n Electrical</span>
      </div>
      <div class="person">
        <p class="person__name">Owen Tate</p>
        <p class="person__role">Qualified Electrician</p>
      </div>
    </header>
    <div class="divider"></div>
    <section class="gallery">
      <div class="gallery__frame"><div class="gallery__photo photo--cables" role="img" aria-label="Photo of stripped electrical cables with copper strands"></div></div>
      <div class="gallery__frame"><div class="gallery__photo photo--spark" role="img" aria-label="Photo of two wire bundles sparking as they meet"></div></div>
      <div class="gallery__frame"><div class="gallery__photo photo--hand" role="img" aria-label="Photo of an open hand with a glowing electric orb"></div></div>
      <div class="gallery__frame"><div class="gallery__photo photo--bulb" role="img" aria-label="Photo of a glowing light bulb on a blue background"></div></div>
    </section>
    <footer class="contact-band">
      <span class="contact-band__item">
        <svg class="icon" viewBox="0 0 24 24" aria-hidden="true"><path d="M6.6 10.8a15.1 15.1 0 0 0 6.6 6.6l2.2-2.2a1 1 0 0 1 1-.25 11.4 11.4 0 0 0 3.6.57 1 1 0 0 1 1 1V20a1 1 0 0 1-1 1A17 17 0 0 1 3 4a1 1 0 0 1 1-1h3.5a1 1 0 0 1 1 1c0 1.25.2 2.45.57 3.57a1 1 0 0 1-.25 1z"/></svg>
        0438257109
      </span>
      <span class="contact-band__sep"></span>
      <span class="contact-band__item">
        <svg class="icon" viewBox="0 0 24 24" aria-hidden="true"><path d="M3 5h18v14H3z" fill="none" stroke="#fff" stroke-width="2"/><path d="M3 5l9 7 9-7" fill="none" stroke="#fff" stroke-width="2"/></svg>
        voltnelectrical@mailbox-example.net
      </span>
      <span class="contact-band__sep"></span>
      <span class="contact-band__item">REC 48193</span>
    </footer>
  </article>
</main>
</body>
</html>
```